2 Funky Pages + EASY stock logo = Construction Website

We would like a funky new website - Just 2 pages - to promote our project management company. A logo is also needed, but we'll provide a stock image which just needs a colour change a text added.

Here are the instructions:

"Fair Tally Homes"

#logo
The one I'd like is attached. Please change font and positioning of text though.

Tagline is "Don't be normal - Be clever"

#Colour combo
756897 Wood Veneer
D5D6D2 sand dollar
353C3F charcoal
962715 brick red

#Home - Page 1

Our cost-price home build service will save you thousands.
No, seriously - Here's how we do it (button)

- Pay what the home building companies do.
- FTH will manage the entire project.
- Use Keystonecraft Guaranteed builders and materials.
- Tender for the best industry rates.
- Get a full budget calculated for the build.
- Avoid inflated 'Fixed-price' builds.
See how it works (button)

Contact Us: 0800 615 278
enquire - Name, Phone, email, comment - SEND

#How it works - Page 2

Traditional fixed price contracts are popular because it means that any risk of unexpected problems is carried by the home builder, but the builder will generally load the price about 10 times above the actual risk carried.

It's like an over-priced insurance policy, on steroids.

Clever people do things differently.

Here's how a cost-price build works...

1) Tell us what you want to build. Dream home, townhouse, investment property, whatever.

2) We'll put a design together for you, or you can choose from a bunch of plans we've already got.

3) We'll give you a conservative price estimate.

4) We finish tweaking your plans, then send them out to our network of more than 200 builders, subcontractors and tradesmen.

5) We collect the quotes, pick the best prices, and finalise your budget. Now you buy us beer, cause you've finally realised how much you're saving.

6) Tell your friends how awesome we are, while we lodge your building consent application with Council.

7) We coordinate the builders and subbies (look, you're already speaking trade-talk) from start to finish. You pay the cost price on their work each month.

We're happy to talk numbers and give you an estimate.

Contact Us: 0800 615 278

Reason: I have seen some great design elements, but need them to come together in one site design. Also, there appears to be less attention paid to the second page design ('how it works') than is necessary... There is no viable contender there yet, compared with the great home page submissions. I've also added some further info to the brief, and note that many submissions have ignored the colour combo I've requested.

Industry/Entity Type

Construction

Number of Pages Required

2 page

Requirements
Must have
• Keystonecrafter logo (small)
• Colour combo described in brief.
Nice to have
• I've attached a stock image I like, but it's certainly not essential. I do like images with clear backgrounds though - they tend to produce a crisp looking site.
• There is a wider image similar to this, available on Pixel Vault, but Sketch Hive won't let me attach it.
Should not have
• Photos of cheesy American faces.

```html
<!DOCTYPE html>
<html lang="en">
<head>
<meta charset="utf-8">
<title>Fair Tally Homes</title>
<link rel="stylesheet" href="https://fonts.googleapis.com/css2?family=Amaranth:wght@400;700&family=Bitter:wght@700&family=Overlock:wght@400;700&display=swap">
<style>
:root{
  --brick:#962715;
  --brick-dark:#7f1f10;
  --charcoal:#11141a;
  --sand:#f3f3f3;
  --ink:#555a5e;
  --white:#ffffff;
  --line:#dcdcdc;
}
*{box-sizing:border-box;margin:0;padding:0}
html,body{width:890px;height:1200px;overflow:hidden}
body{position:relative;background:var(--white);font-family:"Overlock",sans-serif;color:var(--ink)}
.abs{position:absolute}
.header-band{left:0;top:0;width:890px;height:325px;background:var(--brick)}
.brand{left:116px;top:14px;display:flex;align-items:center;gap:10px;color:var(--white)}
.brand-mark{width:52px;height:52px;border:2px solid var(--white)}
.brand-name{font-family:"Amaranth",sans-serif;font-weight:700;font-size:22px;line-height:1}
.brand-tag{font-family:"Amaranth",sans-serif;font-weight:700;font-size:12px;margin-top:4px}
.header-phone{left:522px;top:31px;display:flex;align-items:center;gap:8px;color:var(--white);font-family:"Amaranth",sans-serif;font-style:italic;font-weight:700;font-size:14px;letter-spacing:.5px}
.btn-outline{left:651px;top:29px;width:123px;height:24px;border:1px solid var(--white);color:var(--white);font-size:10.5px;display:flex;align-items:center;justify-content:center;gap:6px;letter-spacing:.3px}
.lower-left{left:0;top:325px;width:445px;height:456px;background:var(--sand)}
.hero-shadow{left:180px;top:380px;width:530px;height:60px;border-radius:50%;background:radial-gradient(ellipse at center,rgba(0,0,0,.28),rgba(0,0,0,0) 70%)}
.hero{left:116px;top:89px;width:658px;height:322px}
.hero-title{left:220px;top:200px;width:450px;text-align:center;color:var(--white);font-family:"Amaranth",sans-serif;font-size:23px;line-height:26px;text-shadow:0 1px 3px rgba(0,0,0,.5)}
.btn-solid{background:var(--brick);color:var(--white);display:flex;align-items:center;justify-content:center;gap:6px}
.hero-cta{left:341px;top:257px;width:208px;height:29px;font-family:"Amaranth",sans-serif;font-size:11.5px}
.hero-arrow{width:27px;height:27px;border:2px solid var(--white);border-radius:50%;top:214px}
.benefits{left:116px;top:460px;width:329px;list-style:none}
.benefit{position:absolute;left:0;width:329px;height:35px;background:var(--white);border:1px solid var(--line);font-size:12px;letter-spacing:.4px;padding-left:17px;display:flex;align-items:center;color:var(--ink)}
.benefit.is-active{background:var(--brick);border-color:var(--brick);color:var(--white);padding-left:22px}
.benefit.is-active::after{content:"";position:absolute;right:-1px;top:10px;border-style:solid;border-width:7px 8px 7px 0;border-color:transparent var(--white) transparent transparent}
.detail-title{left:467px;top:525px;width:300px;text-align:center;color:var(--brick);font-family:"Bitter",serif;font-weight:700;font-size:17px;line-height:21px;letter-spacing:.3px}
.detail-text{left:457px;top:589px;width:320px;text-align:center;font-size:11.5px;line-height:14.5px;letter-spacing:.4px}
.detail-cta{left:552px;top:680px;width:130px;height:24px;font-size:12px;letter-spacing:.3px;border-radius:2px}
.footer{left:0;top:781px;width:890px;height:419px;background:linear-gradient(180deg,#0e1117 0%,#161a22 55%,#1a1c20 100%)}
.footer-title{color:var(--white);font-family:"Amaranth",sans-serif;font-size:17px;top:815px}
.footer-rule{top:847px;width:35px;height:1px;background:var(--white)}
.field{left:116px;width:229px;border:1px solid #cfd2d6;color:var(--white);font-size:9px;padding:5px 7px;letter-spacing:.3px}
.send{left:116px;top:1062px;width:134px;height:24px;font-size:11px;letter-spacing:.3px}
.divider{left:445px;top:819px;width:1px;height:271px;background:#3a3e45}
.contact-row{left:527px;display:flex;align-items:flex-start;gap:14px;color:var(--white)}
.contact-name{font-family:"Amaranth",sans-serif;font-weight:700;font-size:13px}
.contact-addr{font-size:10.5px;line-height:13px;letter-spacing:.4px;margin-top:3px}
.social{top:1046px;width:19px;height:19px;background:#4a4d52}
.social.is-hover{background:#3aaee0}
.foot-line{left:99px;top:1135px;width:694px;height:1px;background:#4a4d52}
.to-top{left:437px;top:1126px;width:19px;height:19px;border:1px solid #6a6d72;border-radius:50%;background:#15181e}
.copyright{left:0;top:1163px;width:890px;text-align:center;color:#cfd2d6;font-family:"Amaranth",sans-serif;font-size:10.5px}
</style>
</head>
<body>
<div class="abs header-band"></div>
<div class="abs lower-left"></div>

<header>
  <div class="abs brand">
    <span class="brand-mark"></span>
    <div><div class="brand-name">Fair Tally Homes</div><div class="brand-tag">Don't be Normal - Be Clever</div></div>
  </div>
  <div class="abs header-phone">
    <svg width="16" height="16" viewBox="0 0 16 16"><path d="M4 1.5l2 3-1.2 1.3c.8 1.8 2.2 3.3 4 4.2L10.1 8.8l3 2-1 2.6c-5.5-.2-10-4.8-10.3-10.3z" fill="none" stroke="#fff" stroke-width="1.3"/><path d="M9.5 2.5a4.5 4.5 0 0 1 4 4M9.5 5a2 2 0 0 1 1.6 1.6" fill="none" stroke="#fff" stroke-width="1.2"/></svg>
    0800 615 278
  </div>
  <div class="abs btn-outline">See how it works
    <svg width="9" height="9" viewBox="0 0 10 10"><circle cx="5" cy="5" r="5" fill="#fff"/><path d="M4 2.8L6.2 5 4 7.2" stroke="#962715" stroke-width="1.4" fill="none"/></svg>
  </div>
</header>

<div class="abs hero-shadow"></div>
<svg class="abs hero" viewBox="0 0 658 322" role="img" aria-label="Photo of a modern two-storey home lit at dusk with a car in the driveway">
  <defs>
    <linearGradient id="heroFill" x1="0" y1="0" x2="0" y2="1">
      <stop offset="0" stop-color="#5f6a70"/>
      <stop offset=".45" stop-color="#3d3a36"/>
      <stop offset=".75" stop-color="#5a4630"/>
      <stop offset="1" stop-color="#2c3328"/>
    </linearGradient>
  </defs>
  <path d="M0 4a4 4 0 0 1 4-4h650a4 4 0 0 1 4 4v238Q329 356 0 242z" fill="#fff"/>
  <path d="M5 6h648v231Q329 345 5 237z" fill="url(#heroFill)"/>
</svg>
<div class="abs hero-arrow" style="left:140px"><svg width="23" height="23" viewBox="0 0 23 23"><path d="M13.5 6.5l-5 5 5 5" stroke="#fff" stroke-width="1.6" fill="none"/></svg></div>
<div class="abs hero-arrow" style="left:723px"><svg width="23" height="23" viewBox="0 0 23 23"><path d="M9.5 6.5l5 5-5 5" stroke="#fff" stroke-width="1.6" fill="none"/></svg></div>
<h1 class="abs hero-title">Our Cost-Price Home Build Service Will Save You Thousands.</h1>
<div class="abs btn-solid hero-cta">No, seriously - Here's how we do it</div>

<ul class="abs benefits">
  <li class="benefit" style="top:0">Use Keystonecraft Guaranteed builders and materials</li>
  <li class="benefit is-active" style="top:47px">Pay what the home building companies do</li>
  <li class="benefit" style="top:95px">FTH will Manage the Entire Project</li>
  <li class="benefit" style="top:142px">Tender for the best industry rate</li>
  <li class="benefit" style="top:189px">Get a full budget calculated for the build</li>
  <li class="benefit" style="top:235px">Avoid inflated 'Fixed-price' builds</li>
</ul>

<h2 class="abs detail-title">Pay what the home building companies do</h2>
<p class="abs detail-text">Lorem Ipsum is simply dummy text of the printing and typesetting industry. Lorem Ipsum has been the industry's standard dummy text ever since</p>
<div class="abs btn-solid detail-cta">See how it works
  <svg width="9" height="9" viewBox="0 0 10 10"><circle cx="5" cy="5" r="5" fill="#fff"/><path d="M4 2.8L6.2 5 4 7.2" stroke="#962715" stroke-width="1.4" fill="none"/></svg>
</div>

<footer>
  <div class="abs footer" role="img" aria-label="Dark night city skyline"></div>
  <h3 class="abs footer-title" style="left:117px">Get in Touch</h3>
  <div class="abs footer-rule" style="left:118px"></div>
  <div class="abs field" style="top:881px;height:24px">Enter your Name</div>
  <div class="abs field" style="top:917px;height:24px">Phone Number</div>
  <div class="abs field" style="top:952px;height:24px">Email</div>
  <div class="abs field" style="top:987px;height:59px">Comment</div>
  <div class="abs btn-solid send">
    <svg width="11" height="11" viewBox="0 0 12 12"><path d="M11 1L1 5.5l3.5 1.3L9 3 5.5 7.6V11l2-2.6 2.2 1.3z" fill="#fff"/></svg>
    Send Your Enquire
  </div>

  <div class="abs divider"></div>

  <h3 class="abs footer-title" style="left:527px">Contact Info</h3>
  <div class="abs footer-rule" style="left:528px"></div>
  <div class="abs contact-row" style="top:877px">
    <svg width="12" height="15" viewBox="0 0 12 15" style="margin:2px 5px 0 0"><path d="M6 0a5 5 0 0 1 5 5c0 3.5-5 10-5 10S1 8.5 1 5a5 5 0 0 1 5-5z" fill="#fff"/><circle cx="6" cy="5" r="1.8" fill="#11141a"/></svg>
    <div><div class="contact-name">Fair Tally Homes</div><div class="contact-addr">96 Lorem Ipsum, giving information<br>origins,&nbsp; as a random Lipsum (8645)</div></div>
  </div>
  <div class="abs contact-row" style="top:947px;align-items:center">
    <svg width="18" height="18" viewBox="0 0 16 16" style="margin-right:5px"><path d="M4 1.5l2 3-1.2 1.3c.8 1.8 2.2 3.3 4 4.2L10.1 8.8l3 2-1 2.6c-5.5-.2-10-4.8-10.3-10.3z" fill="none" stroke="#fff" stroke-width="1.2"/><path d="M9.5 2.5a4.5 4.5 0 0 1 4 4M9.5 5a2 2 0 0 1 1.6 1.6" fill="none" stroke="#fff" stroke-width="1.1"/></svg>
    <span style="font-size:14px;letter-spacing:1px">0800 615 278</span>
  </div>
  <div class="abs contact-row" style="top:990px;align-items:center">
    <svg width="15" height="11" viewBox="0 0 15 11" style="margin-right:8px"><rect width="15" height="11" rx="1" fill="#fff"/><path d="M0 1l7.5 5L15 1" stroke="#11141a" stroke-width="1.2" fill="none"/></svg>
    <span style="font-size:11px;letter-spacing:.4px">info@fairtallyhomes.com</span>
  </div>
  <div class="abs social" style="left:527px"></div>
  <div class="abs social is-hover" style="left:552px"></div>
  <div class="abs social" style="left:577px"></div>

  <div class="abs foot-line"></div>
  <div class="abs to-top"><svg width="17" height="17" viewBox="0 0 17 17"><path d="M5 10l3.5-3.5L12 10" stroke="#9a9da2" stroke-width="1.2" fill="none"/></svg></div>
  <p class="abs copyright">© Copyright 2016 Fair Tally Homes.</p>
</footer>
</body>
</html>
```